Brochure Design Project

A4 Portrait
8 Page Sales brochure for Automatic Coffee Machines for Offices.
We have 4 products in 4 cateries.
Small Office
Medium Office
Large Office
Whole Company / Food Service.

There will be a product image plus 3-4 accessories for each product

Then a brief sales pitch text for each product.

We supply to public listed companies therefore it has to be professional, well presented and eye catching.

Thank you
Updates

I will make the budget $200

Hello,

Please note that I've made changes to the job brief. 

Thanks

Walter 

Hi 

Please find attached contents in pdf for your implementation.

1. Small Office Solution
2. Medium Office Solution 
3. Large Office Solution
4. Whole Company Solution
5. Food Service

Thanks 

Walter

Hi All

Budget increased to $200, extended project by 7 more days.

Thank you

Harold Bensu

Target Market(s)

Big Corporate Companies in major Australian cities

Industry/Entity Type

It Company

Requirements
Must have
• A4 Portrait
8 Page photo and sales pitch text. One product per page starting from 3nd page
5 products into 5 categories of

Page 2 will tell about our company and services

Small Office Solution (page 3)
$16 per day)

Medium Office Solution (page 4)
$18 per day)

Large Office Solution (page 5)
$19 per day)

Whole Company (page 6)
$24 per day)

Food Service Solution (page 7
$28 per day

Each product page will highlight
eg
Small Office Solution
$16 per day)

Each page will have 3-4 accessories (photos)

Page 8 Our logo, address & Conatct details - Please see for contact details http://www.brewnova.com.au/brew_nova
Nice to have
• Logo, photo of coffee machine, an office environment where people are kind of enjoying coffee in a lounge.

Should not have
• Not messy, no old style,

```html
<!DOCTYPE html>
<html lang="en">
<head>
<meta charset="utf-8">
<title>Whole Company Solution and Food Service Brochure Spread</title>
<link href="https://fonts.googleapis.com/css2?family=Open+Sans:wght@400;600;700;800&family=Roboto+Condensed:wght@700&display=swap" rel="stylesheet">
<style>
  :root {
    --brand-red: #d3172a;
    --brand-red-dark: #9e0f1d;
    --ink: #1e1e1e;
    --ink-soft: #555555;
    --panel-grey: #ececec;
    --page-white: #ffffff;
    --backdrop: #e6e6e6;
    --photo-light: #d9d9d9;
    --photo-dark: #6b6b6b;
  }
  * { box-sizing: border-box; margin: 0; padding: 0; }
  html, body { width: 1200px; height: 800px; overflow: hidden; }
  body {
    background: var(--backdrop);
    font-family: "Open Sans", Arial, sans-serif;
    color: var(--ink);
  }
  .spread {
    position: absolute; left: 63px; top: 20px;
    width: 1074px; height: 760px;
    display: flex;
    box-shadow: 0 6px 24px rgba(0,0,0,.18);
  }
  .page {
    position: relative; width: 537px; height: 760px;
    background: var(--page-white); overflow: hidden;
  }
  .page--left { border-right: 1px solid #dcdcdc; }

  .top-ribbon { position: absolute; left: 0; top: 0; width: 537px; height: 48px; }
  .ribbon-title {
    position: absolute; top: 12px; right: 24px;
    font-family: "Roboto Condensed", "Arial Narrow", sans-serif;
    font-size: 15px; color: #fff; letter-spacing: .5px; text-transform: uppercase;
  }

  .section-title {
    font-family: "Roboto Condensed", "Arial Narrow", sans-serif;
    color: var(--brand-red); font-size: 13px; text-transform: uppercase;
    display: flex; align-items: center; gap: 6px;
  }
  .section-title::before {
    content: ""; width: 0; height: 0;
    border-left: 7px solid var(--brand-red);
    border-top: 5px solid transparent; border-bottom: 5px solid transparent;
  }

  .intro { position: absolute; left: 24px; top: 60px; width: 490px; }
  .intro__title {
    font-family: "Roboto Condensed", "Arial Narrow", sans-serif;
    color: var(--brand-red); font-size: 16px; line-height: 1.3; text-transform: uppercase;
  }
  .intro__lead { font-size: 11px; font-weight: 700; margin-top: 2px; line-height: 1.35; }
  .intro__dims { font-size: 8px; font-weight: 600; margin-top: 5px; color: var(--ink-soft); }
  .spec-columns { display: flex; gap: 20px; margin-top: 7px; }
  .spec-list { list-style: disc; padding-left: 14px; font-size: 10px; font-weight: 700; line-height: 1.33; width: 225px; }
  .spec-list--plain { list-style: none; padding-left: 12px; }

  .price-badge {
    position: absolute; background: var(--brand-red); color: #fff;
    font-family: "Roboto Condensed", "Arial Narrow", sans-serif;
    font-size: 13px; padding: 6px 16px; border-radius: 12px 0 12px 0;
    text-transform: uppercase;
  }

  .features { position: absolute; left: 24px; top: 342px; width: 250px; }
  .features__panel {
    margin-top: 8px; background: var(--panel-grey);
    padding: 11px 12px 4px; border-radius: 0 0 14px 0;
  }
  .feature { margin-bottom: 9px; }
  .feature__name { font-size: 8.5px; font-weight: 800; color: var(--ink); text-transform: uppercase; }
  .feature__name span { color: var(--brand-red); margin-right: 3px; }
  .feature__text { font-size: 8px; line-height: 1.4; color: var(--ink-soft); margin-top: 2px; }

  .photo-frame {
    position: absolute; border: 2px solid var(--brand-red);
    border-radius: 14px 0 14px 0; padding: 6px; background: #fff;
  }
  .photo-fill {
    width: 100%; height: 100%; border-radius: 8px 0 8px 0;
    background: linear-gradient(160deg, var(--photo-light), #f4f4f4 45%, var(--photo-dark));
  }
  .photo-fill--dark { background: linear-gradient(170deg, #f2f2f2 0%, #bdbdbd 45%, #2c2c2c 100%); }

  .page-pill {
    position: absolute; bottom: 22px; right: 22px;
    background: var(--brand-red); color: #fff;
    font-size: 9px; font-weight: 700; padding: 4px 14px;
    border-radius: 10px 0 10px 0; text-transform: uppercase;
  }

  .text-column { position: absolute; top: 62px; width: 232px; }
  .body-copy { font-size: 9px; line-height: 1.5; margin: 5px 0 10px; font-weight: 600; }

  .consistency { position: absolute; left: 24px; top: 262px; width: 232px; }
  .consistency__panel {
    margin-top: 46px; background: var(--panel-grey);
    padding: 12px; border-radius: 0 0 14px 0;
  }
  .consistency__item { font-size: 8px; line-height: 1.45; color: var(--ink-soft); margin-bottom: 8px; }
  .consistency__item span { color: var(--brand-red); font-weight: 800; }

  .bottom-wave { position: absolute; left: 0; bottom: 0; width: 537px; height: 120px; }
</style>
</head>
<body>
<main class="spread">

  <section class="page page--left">
    <svg class="top-ribbon" viewBox="0 0 537 48" aria-hidden="true">
      <path d="M0 46 L537 46" stroke="var(--brand-red)" stroke-width="1.5"/>
      <path d="M250 0 H537 V40 H290 Q270 40 262 30 Z" fill="var(--brand-red)"/>
    </svg>
    <div class="ribbon-title">Whole Company Solution</div>

    <div class="intro">
      <h1 class="intro__title">Whole Company Solution</h1>
      <p class="intro__lead">The choice of Harbourline Diners restaurants worldwide.</p>
      <p class="intro__dims">Coffee Machine Dimension: W: 600 // D: 600 // H: 700</p>
      <div class="spec-columns">
        <ul class="spec-list">
          <li>Fresh Coffee;</li>
          <li>Fresh Milk;</li>
          <li>Automated Cleaning Program: No parts removed and no manuals required;</li>
          <li>16 Drinks of your choice;</li>
          <li>Easy Operation;</li>
        </ul>
        <ul class="spec-list">
          <li>Fast and Quiet;</li>
          <li>Robust Body &amp; Metal Brewer;</li>
          <li>HACCP Certified;</li>
          <li>Café Quality Drinks;</li>
          <li>Up to 16 selections including:</li>
          <li class="spec-list--plain">Cappuccino<br>Hot Chocolate<br>Espresso<br>Latte<br>Mocha<br>Chai Latte</li>
          <li>Strength and cup size options.</li>
        </ul>
      </div>
    </div>

    <div class="price-badge" style="left:196px; top:312px;">$24 Per Day</div>

    <div class="features">
      <h2 class="section-title">Features</h2>
      <div class="features__panel">
        <div class="feature">
          <p class="feature__name"><span>01.</span>Fresh Coffee - Whole Bean Brewer</p>
          <p class="feature__text">Beans are ground fresh for every cup, giving a rich aroma and a full café taste for all staff and visitors.</p>
        </div>
        <div class="feature">
          <p class="feature__name"><span>02.</span>Fully Automated Cleaning Program - HACCP Certified</p>
          <p class="feature__text">The machine rinses and cleans itself each day, so no parts are removed and no manual work is needed.</p>
        </div>
        <div class="feature">
          <p class="feature__name"><span>03.</span>Easy Operation - Graphic Display</p>
          <p class="feature__text">A clear touch display guides every user to the right drink in seconds, with no training required.</p>
        </div>
        <div class="feature">
          <p class="feature__name"><span>04.</span>Hot Chocolate</p>
          <p class="feature__text">A separate powder unit mixes smooth hot chocolate and adds variety to the menu for every taste.</p>
        </div>
        <div class="feature">
          <p class="feature__name"><span>05.</span>Automated Quality Coffee System - Consistent</p>
          <p class="feature__text">Each cup is brewed to the same recipe, keeping strength, temperature and milk texture steady all day.</p>
        </div>
        <div class="feature">
          <p class="feature__name"><span>06.</span>Choices</p>
          <p class="feature__text">Strength and cup size can be set for every drink, from a small espresso to a large latte.</p>
        </div>
      </div>
    </div>

    <div class="photo-frame" style="left:290px; top:350px; width:224px; height:160px;">
      <div class="photo-fill" role="img" aria-label="Photo of the whole company automatic coffee machine"></div>
    </div>
    <div class="photo-frame" style="left:290px; top:520px; width:108px; height:104px;">
      <div class="photo-fill" role="img" aria-label="Photo of a cup and milk accessory cabinet"></div>
    </div>
    <div class="photo-frame" style="left:406px; top:520px; width:108px; height:104px;">
      <div class="photo-fill" role="img" aria-label="Photo of a stainless steel milk cooler accessory"></div>
    </div>

    <div class="page-pill">Page 06 of 08</div>
  </section>

  <section class="page page--right">
    <svg class="top-ribbon" viewBox="0 0 537 48" aria-hidden="true">
      <path d="M0 46 L537 46" stroke="var(--brand-red)" stroke-width="1.5"/>
      <path d="M300 0 H537 V40 H340 Q320 40 312 30 Z" fill="var(--brand-red)"/>
    </svg>
    <div class="ribbon-title">Food Service</div>

    <div class="text-column" style="left:24px;">
      <h2 class="section-title">Why Automatic Coffee Machine</h2>
      <p class="body-copy">Staff spend less time away from their desks when great coffee is close at hand. An automatic machine serves café quality drinks at the touch of a button, every day of the week.</p>
      <h2 class="section-title">Café Quality</h2>
      <p class="body-copy">The bar for coffee quality has been set by cafés.</p>
    </div>
    <div class="text-column" style="left:282px;">
      <p class="body-copy" style="margin-top:0;">With fresh beans and fresh milk, every cup matches what your team would buy down the street, without the queue or the cost.</p>
      <h2 class="section-title">How It Works</h2>
      <p class="body-copy">Beans are ground, brewed and topped with steamed milk in under a minute. Service visits and supplies are all included in one simple daily price.</p>
    </div>

    <div class="consistency">
      <h2 class="section-title">Consistency</h2>
      <div class="consistency__panel">
        <p class="consistency__item"><span>01.</span> Same recipe, same taste, cup after cup for every user.</p>
        <p class="consistency__item"><span>02.</span> Milk is frothed to the same texture all day long.</p>
        <p class="consistency__item"><span>03.</span> Drink sizes are set once and kept for every order.</p>
      </div>
    </div>
    <div class="price-badge" style="left:110px; top:288px;">$19 Per Day</div>

    <div class="photo-frame" style="left:282px; top:262px; width:232px; height:230px;">
      <div class="photo-fill photo-fill--dark" role="img" aria-label="Photo of the food service coffee machine on a counter"></div>
    </div>

    <svg class="bottom-wave" viewBox="0 0 537 120" aria-hidden="true">
      <path d="M0 120 C180 110 360 70 537 10 V120 Z" fill="var(--brand-red)"/>
      <path d="M0 120 C200 114 380 90 537 50 V120 Z" fill="var(--brand-red-dark)"/>
    </svg>
    <div class="page-pill" style="bottom:auto; top:520px;">Page 07 of 08</div>
  </section>

</main>
</body>
</html>
```